Need App for Impact Related Events

My app is to help with internal events. When you enter the prompted event code the next screen shows you everyone currently at the event. It will give you the ability to Start a conversation with someone you met at that event, or signal it is your turn to send a message. The next screen is a message thread with that person. I am looking for a design that incorporates the colors and ‘feel good’ emotion of our logo. I have pieced together a pretty good interpretation of what I’m looking for in the attached mockup by slicing and dicing designs. I also attached our logo mascot.Screens (see attached mockups)

Note 1: I do not like the picture on the screen used in screen one because it makes it seem like a dating app. I attached an alternative photo that can be used or present different ideas.

Note 2: On the login/signup screen (screen 2) I need an additional first and last name for login, you can try to fit this on one login screen or present a two step signup screen where that is presented in the second screen.

READ MOCKUP GUIDELINES UNDER Must Haves

Target Market(s)

People attending internal social impact events

Industry/Entity Type

Charity

Font styles to use
Sans Serif

Colors
86cfc6

Requirements
Must have
• Follow the screen mockups attached to project
• PLEASE READ
• I have provided a relatively close design of what I’m looking for in the mockups. Some screens need to be followed more closely to my design mockup than other. I have listed a guide below how how closely you should follow my mockup design exactly. Overall I would like to see some ideas of incorporating a few accent colors so it doesn’t appear SO Blue. I also attached some app inspiration designs I found from around the web
• Screen Mockup Guideline Follow %
• Screen 1: 65% - mostly on target, would like to see ways to make it not SO Blue and possibly creative places to add some explainer text describing the app
• Screen 2: 50% - general design idea is here, but more open
• Screen 3: 35% - a lot more room for design influence
• Screen 4: 70% - mostly on target, a little room for design influence/color scheme ideas
• Screen 5-6: 25% - a lot of room for design change/ideas/influence
• Screen 7-8: 80% - already very close to what I need, maybe open to slight sizing and color scheme ideas
• Screen 9: 15% - the most open for influence, only the general functionality of the screen is communicated here
Nice to have
• Please Read Mockup Guideline above. In large part I am looking for something to use some nice accent colors so it is not overwhelmingly blue and bring the whole design into a seamless style.
Should not have

```html
<!DOCTYPE html>
<html lang="en">
<head>
<meta charset="utf-8">
<title>Who you've met – People screen</title>
<link href="https://fonts.googleapis.com/css2?family=Montserrat:wght@400;500;600;700&display=swap" rel="stylesheet">
<style>
  :root {
    --canvas-bg: #e9ebec;
    --screen-bg: #f1f2f3;
    --header-start: #27b2d9;
    --header-end: #5ee3e2;
    --white: #ffffff;
    --card-under: #e4e6e8;
    --text-dark: #2b2e33;
    --text-muted: #9a9ea3;
    --start-green: #4fcf95;
    --turn-blue: #27aed6;
    --tab-active: #3cc1d6;
    --tab-idle: #8c9095;
    --avatar-tone: #8a5a45;
    --avatar-ring: #d9dcdf;
  }
  * { box-sizing: border-box; margin: 0; padding: 0; }
  html, body {
    width: 1200px; height: 893px; overflow: hidden;
    background: var(--canvas-bg);
    font-family: "Montserrat", sans-serif;
  }
  .stage { position: relative; width: 1200px; height: 893px; }

  .app-screen {
    position: absolute; left: 366px; top: 30px;
    width: 375px; height: 667px;
    transform: scale(1.25); transform-origin: top left;
    background: var(--screen-bg);
    overflow: hidden;
    box-shadow: 0 4px 20px rgba(0,0,0,.08);
  }

  /* Header */
  .app-header {
    height: 108px;
    background: linear-gradient(90deg, var(--header-start), var(--header-end));
    color: var(--white);
    position: relative;
  }
  .status-bar {
    height: 20px; display: flex; align-items: center; justify-content: space-between;
    padding: 0 6px; font-size: 11px; font-weight: 500;
  }
  .status-left, .status-right { display: flex; align-items: center; gap: 4px; width: 110px; }
  .status-right { justify-content: flex-end; }
  .status-time { font-weight: 600; }
  .screen-title {
    text-align: center; font-size: 17px; font-weight: 600; margin-top: 12px;
  }
  .tab-switch {
    position: absolute; bottom: 0; left: 0; right: 0;
    display: flex; height: 36px;
  }
  .tab-switch__item {
    flex: 1; text-align: center; font-size: 11px; font-weight: 700;
    letter-spacing: .8px; line-height: 30px; opacity: .8;
  }
  .tab-switch__item--active { opacity: 1; border-bottom: 3px solid var(--white); }

  /* People list */
  .people-count {
    text-align: center; font-size: 11px; color: var(--text-muted);
    margin: 10px 0 8px;
  }
  .people-list { list-style: none; padding: 0 12px; }
  .person-card {
    position: relative; height: 78px; margin-bottom: 8px;
  }
  .person-card::after {
    content: ""; position: absolute; left: 10px; right: 10px; top: 8px; bottom: -6px;
    background: var(--card-under); border-radius: 10px; z-index: 0;
  }
  .person-card__body {
    position: relative; z-index: 1; height: 100%;
    background: var(--white); border-radius: 10px;
    box-shadow: 0 2px 6px rgba(0,0,0,.06);
    display: flex; align-items: center; padding: 0 14px;
  }
  .person-card__avatar {
    width: 46px; height: 46px; border-radius: 50%;
    background: radial-gradient(circle at 50% 45%, #c99a83 0%, var(--avatar-tone) 70%);
    border: 2px solid var(--avatar-ring); flex-shrink: 0;
  }
  .person-card__info { margin-left: 14px; flex: 1; }
  .person-card__name { font-size: 15px; font-weight: 500; color: var(--text-dark); }
  .person-card__meta { font-size: 11px; color: var(--text-muted); margin-top: 3px; }

  .action-btn {
    width: 78px; height: 52px; border-radius: 6px; border: none;
    color: var(--white); font-family: inherit; font-size: 12px; font-weight: 500;
    display: flex; flex-direction: column; align-items: center; justify-content: center; gap: 4px;
  }
  .action-btn--start { background: var(--start-green); }
  .action-btn--turn { background: var(--turn-blue); }

  /* Tab bar */
  .tab-bar {
    position: absolute; left: 0; right: 0; bottom: 0; height: 50px;
    background: var(--white); border-top: 1px solid #e2e4e6;
    display: flex;
  }
  .tab-bar__item {
    flex: 1; display: flex; flex-direction: column; align-items: center; justify-content: center;
    font-size: 9px; color: var(--tab-idle); gap: 3px;
  }
  .tab-bar__item--active { color: var(--tab-active); }
</style>
</head>
<body>
<div class="stage">
  <div class="app-screen">
    <header class="app-header">
      <div class="status-bar">
        <div class="status-left">
          <svg width="18" height="8" viewBox="0 0 18 8"><g fill="#fff"><circle cx="2" cy="4" r="2"/><circle cx="6.5" cy="4" r="2"/><circle cx="11" cy="4" r="2"/><circle cx="15.5" cy="4" r="2" opacity=".5"/></g></svg>
          <span>Carrier</span>
          <svg width="12" height="9" viewBox="0 0 12 9"><path d="M6 9 0 3a8.5 8.5 0 0 1 12 0z" fill="#fff"/></svg>
        </div>
        <span class="status-time">9:41 AM</span>
        <div class="status-right">
          <svg width="6" height="10" viewBox="0 0 6 10"><path d="M1 3l4 4-2 2V1l2 2-4 4" fill="none" stroke="#fff" stroke-width="1"/></svg>
          <span>100%</span>
          <svg width="22" height="10" viewBox="0 0 22 10"><rect x=".5" y=".5" width="19" height="9" rx="2" fill="none" stroke="#fff"/><rect x="2" y="2" width="16" height="6" rx="1" fill="#fff"/><rect x="20" y="3" width="1.5" height="4" fill="#fff"/></svg>
        </div>
      </div>
      <h1 class="screen-title">Who you've met</h1>
      <nav class="tab-switch">
        <span class="tab-switch__item tab-switch__item--active">FOR YOU</span>
        <span class="tab-switch__item">POPULAR</span>
      </nav>
    </header>

    <p class="people-count">31 People to meet</p>

    <ul class="people-list">
      <li class="person-card"><div class="person-card__body">
        <div class="person-card__avatar" role="img" aria-label="Profile photo of attendee"></div>
        <div class="person-card__info"><p class="person-card__name">Dana R.</p><p class="person-card__meta">Has met 6 people</p></div>
        <button class="action-btn action-btn--start">
          <svg width="14" height="16" viewBox="0 0 14 16"><path d="M2 15V1M2 1.5h10l-2.5 3.5L12 8.5H2" fill="none" stroke="#fff" stroke-width="1.4" stroke-linejoin="round"/></svg>Start</button>
      </div></li>
      <li class="person-card"><div class="person-card__body">
        <div class="person-card__avatar" role="img" aria-label="Profile photo of attendee"></div>
        <div class="person-card__info"><p class="person-card__name">Dana R.</p><p class="person-card__meta">Has met 6 people</p></div>
        <button class="action-btn action-btn--turn">
          <svg width="14" height="14" viewBox="0 0 14 14"><path d="M2 13V6h9M8 3l3 3-3 3" fill="none" stroke="#fff" stroke-width="1.4" stroke-linejoin="round"/></svg>Your turn</button>
      </div></li>
      <li class="person-card"><div class="person-card__body">
        <div class="person-card__avatar" role="img" aria-label="Profile photo of attendee"></div>
        <div class="person-card__info"><p class="person-card__name">Dana R.</p><p class="person-card__meta">Has met 6 people</p></div>
        <button class="action-btn action-btn--start">
          <svg width="14" height="16" viewBox="0 0 14 16"><path d="M2 15V1M2 1.5h10l-2.5 3.5L12 8.5H2" fill="none" stroke="#fff" stroke-width="1.4" stroke-linejoin="round"/></svg>Start</button>
      </div></li>
      <li class="person-card"><div class="person-card__body">
        <div class="person-card__avatar" role="img" aria-label="Profile photo of attendee"></div>
        <div class="person-card__info"><p class="person-card__name">Dana R.</p><p class="person-card__meta">Has met 6 people</p></div>
      </div></li>
      <li class="person-card"><div class="person-card__body">
        <div class="person-card__avatar" role="img" aria-label="Profile photo of attendee"></div>
        <div class="person-card__info"><p class="person-card__name">Dana R.</p><p class="person-card__meta">Has met 6 people</p></div>
      </div></li>
    </ul>

    <nav class="tab-bar">
      <div class="tab-bar__item tab-bar__item--active">
        <svg width="18" height="14" viewBox="0 0 18 14" fill="none" stroke="currentColor" stroke-width="1.3"><circle cx="6.5" cy="4" r="3"/><path d="M1 13c0-3 2.5-5 5.5-5s5.5 2 5.5 5z"/><circle cx="12.5" cy="4" r="2.5"/><path d="M13 8c2.5 0 4 2 4 5h-3"/></svg>
        People</div>
      <div class="tab-bar__item">
        <svg width="16" height="14" viewBox="0 0 16 14" fill="none" stroke="currentColor" stroke-width="1.3"><path d="M2 1h12a1 1 0 0 1 1 1v7a1 1 0 0 1-1 1H7l-3 3v-3H2a1 1 0 0 1-1-1V2a1 1 0 0 1 1-1z"/></svg>
        Chats</div>
      <div class="tab-bar__item">
        <svg width="15" height="15" viewBox="0 0 16 16" fill="none" stroke="currentColor" stroke-width="1.3"><circle cx="8" cy="8" r="2.5"/><path d="M8 1v2M8 13v2M1 8h2M13 8h2M3 3l1.4 1.4M11.6 11.6 13 13M3 13l1.4-1.4M11.6 4.4 13 3"/><circle cx="8" cy="8" r="5"/></svg>
        Settings</div>
    </nav>
  </div>
</div>
</body>
</html>
```